Gablestone Inspections Business Card

I need a business card for my new company. The company is going to provide home inspections. The name of the company is Gablestone Inspections. I am not sure if I want a single sided card or a double. I have a logo already that I want to incorporate into the card design. I was wondering if I should incorporate a catch phrase on my card or not. If I did the phrase would be "The Intelligent Choice for Home Inspections" but i am unsure how or if to use it on a card. The following information needs to be on the card.
Home Inspection
My Name: Tobias R. Fenwick Phone Number: 555-317-6420 Email: tfenwick@gablestoneinspections.com Website: www.gablestoneinspections.com NY HI License # 27300592415

```html
<!DOCTYPE html>
<html lang="en">
<head>
<meta charset="utf-8">
<title>Gablestone Inspections – Business Card</title>
<link href="https://fonts.googleapis.com/css2?family=Montserrat:wght@400;500;700&display=swap" rel="stylesheet">
<style>
  :root {
    --bg: #dcdcdc;
    --card: #262626;
    --card-deep: #1d1d1d;
    --accent: #5cb8ec;
    --white: #ffffff;
    --muted: #d6d6d6;
    --rule: #9a9a9a;
  }
  * { margin: 0; padding: 0; box-sizing: border-box; }
  html, body { width: 1200px; height: 801px; overflow: hidden; }
  body {
    background: var(--bg);
    font-family: "Montserrat", Arial, sans-serif;
    position: relative;
  }
  .card {
    position: absolute;
    top: 252px;
    width: 520px;
    height: 297px;
    background: var(--card);
    border: 3px solid var(--accent);
    overflow: hidden;
    color: var(--white);
  }
  .card--front { left: 60px; }
  .card--back { left: 620px; }

  /* Front */
  .brand {
    position: absolute;
    right: 34px;
    top: 46px;
    display: flex;
    align-items: center;
    gap: 10px;
    font-weight: 700;
    font-size: 21px;
    color: var(--white);
    letter-spacing: 0.3px;
  }
  .brand__mark { width: 14px; height: 14px; background: var(--accent); }
  .accent-bar {
    position: absolute; left: 0; top: 130px;
    width: 8px; height: 50px; background: var(--accent);
  }
  .person { position: absolute; left: 30px; top: 130px; }
  .person__name { font-weight: 700; font-size: 25px; color: var(--accent); line-height: 1.1; }
  .person__title { font-weight: 500; font-size: 11px; letter-spacing: 0.6px; margin-top: 4px; }
  .divider {
    position: absolute; left: 30px; right: 34px; top: 185px;
    height: 1px; background: var(--rule);
  }
  .contacts { position: absolute; left: 30px; top: 198px; list-style: none; }
  .contacts li {
    display: flex; align-items: center; gap: 9px;
    font-size: 13px; color: var(--muted); height: 21px;
  }
  .contacts svg { width: 13px; height: 13px; flex: none; }
  .license {
    position: absolute; right: 34px; top: 200px;
    text-align: right; font-size: 12.5px; color: var(--muted); line-height: 1.6;
  }

  /* Back */
  .pattern {
    position: absolute; inset: 0;
    background: linear-gradient(120deg, #2a2a2a 0%, #1f1f1f 45%, #2d2d2d 70%, #1c1c1c 100%);
  }
  .back-brand {
    position: absolute; left: 0; right: 0; top: 104px;
    display: flex; justify-content: center; align-items: center; gap: 10px;
    font-weight: 700; font-size: 22px; color: var(--white);
  }
  .back-brand__mark { width: 14px; height: 14px; background: var(--accent); }
  .tagline {
    position: absolute; left: 0; right: 0; top: 178px;
    text-align: center; font-size: 15px; color: var(--white); letter-spacing: 0.3px;
  }
</style>
</head>
<body>
  <section class="card card--front">
    <div class="brand"><span class="brand__mark"></span>Gablestone Inspections</div>
    <div class="accent-bar"></div>
    <div class="person">
      <div class="person__name">Tobias R. Fenwick</div>
      <div class="person__title">MANAGING DIRECTOR</div>
    </div>
    <div class="divider"></div>
    <ul class="contacts">
      <li>
        <svg viewBox="0 0 16 16"><circle cx="8" cy="8" r="8" fill="var(--accent)"/><path d="M5 4.5l1.6-.3.9 2-1 .8a5 5 0 0 0 2.5 2.5l.8-1 2 .9-.3 1.6c-3.6.3-6.8-2.9-6.5-6.5z" fill="var(--card)"/></svg>
        555-317-6420
      </li>
      <li>
        <svg viewBox="0 0 16 16"><rect x="1" y="3" width="14" height="10" fill="var(--accent)"/><path d="M1 3l7 6 7-6" fill="none" stroke="var(--card)" stroke-width="1.3"/></svg>
        tfenwick@gablestoneinspections.com
      </li>
      <li>
        <svg viewBox="0 0 16 16"><circle cx="8" cy="8" r="7" fill="var(--accent)"/><path d="M1 8h14M8 1c-3 3-3 11 0 14M8 1c3 3 3 11 0 14" fill="none" stroke="var(--card)" stroke-width="1"/></svg>
        www.gablestoneinspections.com
      </li>
    </ul>
    <div class="license">NY HI<br>License # 27300592415</div>
  </section>

  <section class="card card--back">
    <div class="pattern" role="img" aria-label="Faint repeating company emblem pattern in dark grey"></div>
    <div class="back-brand"><span class="back-brand__mark"></span>Gablestone Inspections</div>
    <p class="tagline">The Intelligent Choice for Home Inspections</p>
  </section>
</body>
</html>
```